Business Card for a Life Coaching Company

BRAVOPEAK is a Life Coaching company that was initiated to support people who want to transform thier life or ana aspect of it.
our slogan is : "Dream. Believe. Succeed"
our logo is uploaded.
The name of the company implies that leadership, strength and wisdom required to change your life.
We want an attractive business card that would give an impression of reliability, support and change. so we really want it unique. Here are some examples of unique cards:

http://www.cardcraftvault.example/2009/05/100-really-creative-business-cards/

BravoPeak is a life coaching organization focusing on individual transformation through the application of relevant and timeless principles of success.  BravoPeak believes that real, sustainable life transformations are brought about by tuning into the timeless wisdom we each carry in our hearts while boldy acting in the direction of our dreams.

Contacts on the card:
Address: 7 Tarek Nour El Dine Heliopolis Cairo Egypt
Tel: +202 24 71 38 52
Fax: +202 24 71 38 17
Mobile: +2 012 684 2097 (Dalia Soliman)
+2 0199915815 (Tariq Bhatti)

By the way, our temporary website is http://www.bravopeak.example

We have attached an .eps file with various configurations of our logo.

```html
<!DOCTYPE html>
<html lang="en">
<head>
<meta charset="utf-8">
<title>BravoPeak Business Card</title>
<link rel="stylesheet" href="https://fonts.googleapis.com/css2?family=Open+Sans:wght@400;600;700&display=swap">
<style>
  :root {
    --accent: #f15a29;
    --accent-light: #f7895f;
    --ink: #555555;
    --ink-soft: #666666;
    --frame: #cfcfcf;
    --ghost: #efefef;
    --ghost-edge: #f8f8f8;
    --paper: #ffffff;
  }
  * { box-sizing: border-box; margin: 0; padding: 0; }
  html, body {
    width: 1200px;
    height: 1158px;
    overflow: hidden;
    background: var(--paper);
    font-family: "Open Sans", Arial, sans-serif;
  }
  .canvas { position: relative; width: 1200px; height: 1158px; }
  .card {
    position: absolute;
    left: 246px;
    width: 696px;
    height: 420px;
    border: 2px solid var(--frame);
    background: var(--paper);
    overflow: hidden;
  }
  .card--front { top: 96px; }
  .card--back { top: 610px; }

  .holder { position: absolute; left: 24px; top: 32px; }
  .holder__name { color: var(--accent); font-weight: 700; font-size: 27px; line-height: 34px; }
  .holder__role { color: var(--ink); font-size: 19px; line-height: 26px; }
  .holder__mobile { color: var(--ink); font-size: 17px; line-height: 26px; }

  .contact { position: absolute; left: 24px; top: 202px; color: var(--ink); font-size: 19px; line-height: 30px; }
  .contact strong { font-weight: 700; }
  .contact__web { color: var(--accent); }

  .artwork--lion {
    position: absolute;
    left: 464px;
    top: 8px;
    width: 232px;
    height: 412px;
    border-radius: 120px 40px 0 0;
    background: linear-gradient(160deg, var(--accent-light), var(--accent));
  }
  .artwork--ghost {
    position: absolute;
    left: 464px;
    top: 4px;
    width: 232px;
    height: 414px;
    border-radius: 120px 40px 0 0;
    background: linear-gradient(160deg, var(--ghost-edge), var(--ghost));
  }

  .brand {
    position: absolute;
    left: 0;
    right: 0;
    top: 144px;
    display: flex;
    justify-content: center;
    align-items: center;
    gap: 12px;
  }
  .brand__mark { width: 30px; height: 30px; background: var(--accent); }
  .brand__name { color: var(--ink-soft); font-size: 34px; font-weight: 400; letter-spacing: 1px; }

  .slogan {
    position: absolute;
    left: 0;
    right: 0;
    top: 232px;
    text-align: center;
    color: var(--ink-soft);
    font-size: 31px;
  }
  .slogan__dot { color: var(--accent); font-weight: 700; }
</style>
</head>
<body>
<main class="canvas">
  <section class="card card--front">
    <div class="holder">
      <p class="holder__name">Dalia Soliman</p>
      <p class="holder__role">designation</p>
      <p class="holder__mobile">M: +2 012 684 2097</p>
    </div>
    <div class="contact">
      <p>7 Tarek Nour El Dine Heliopolis Cairo Egypt</p>
      <p><strong>T:</strong> +202 24 71 38 52 | <strong>F:</strong> +202 24 71 38 17</p>
      <p>W: <span class="contact__web">www.bravopeak.example</span></p>
    </div>
    <div class="artwork--lion" role="img" aria-label="Orange illustration of a lion's head in profile"></div>
  </section>

  <section class="card card--back">
    <div class="artwork--ghost" role="img" aria-label="Faint grey lion head illustration as background decoration"></div>
    <div class="brand">
      <span class="brand__mark"></span>
      <span class="brand__name">BRAVOPEAK</span>
    </div>
    <p class="slogan">Dream <span class="slogan__dot">.</span> Believe <span class="slogan__dot">.</span> Succeed</p>
  </section>
</main>
</body>
</html>
```